Logo & Business card - Want to paint the town?

Brushvane - Top Quality Painting & Decorating

Brushvane are a painting & decorating company who work predominantly in the residential market and not commercial. We require a logo and business cards design

The company is based Christchurch NZ. Christchurch had major earthquakes in 2010 and 2011, which devastated the city. The city is in rebuild and fixing phase and will be for the next 5 years to get the city back on it's feet. As a result of the earthquakes are a lot of homes being fixed that require painting and decorating.

Additional to the earthquake work there is also huge growth in the city meaning lots of new homes are being built to accommodate the growth.

Alongside this there is an every growing rental market, so we not only work on residential earthquake repairs and new builds but also work with real estate agents, property managers and interior designers.

Christchurch has seen a large number of tradesmen enter the market and not all of whom are qualified/skilled. Our company’s painters are those with years of experience and who pride themselves on top quality precision work.

Brushvane are about quality jobs, done to a very high level at an affordable price. We are not the cheapest but also not the most expensive. Our logo and cards must reflect the quality of our work. Brushvane requires a professional logo and business card targeted to the higher end of the residential market.

Target Market(s)

Builders requiring contract painters, housing companies such as Tom Halvey, Kestrel buildings, Harbor Nest etc., real estate agents, property managers, interior designers and home owners.

The business cards and logo must appeal to builders, homeowner, interior designers and real estate agents so can’t be too masculine/feminine.

It needs to be bold, professional and stylish.

Industry/Entity Type

Residential

Logo Text

Brushvane

Logo styles of interest
Wordmark Logo
Requirements
Must have
• The logo and business cards must be bold, clean, modern, smart, simple, self explanatory, tidy, easy to read, timeless, and not frilly.

We are about quality, precision and being able to cut a straight line, so the card needs to avoid and curvy brush strokes as this denotes a bad a and sloppy painter.

The card and logo must scream top quality and affordability.
The card must be clean and modern, high end and stylish.

The logo must be something, which will go well on a silver/ black background as eventually as the van fleet will be either silver or black, so it must punch out on these colours.

For contact details that need to appear on the business cards see the full brief attached.
Nice to have
• One idea could be to have a picture on the business card of a well-painted stylish modern home interior, which would eventually be replaced by picture of Brushvane's paint jobs.
Should not have
• It definitely must not include is paint drips; paint pot with dribbles over the side of it, splurges of paint, or paintbrush swooshes as this indicates a messy painter.

Most colours are ok except for pink, orange or pastel colours.

```html
<!DOCTYPE html>
<html lang="en">
<head>
<meta charset="utf-8">
<title>Brushvane – Business Cards</title>
<link rel="stylesheet" href="https://fonts.googleapis.com/css2?family=Roboto:wght@300;400;700&display=swap">
<style>
  :root {
    --page-bg: #e7e1db;
    --card-brown: #3b2d22;
    --cream: #f6efd6;
    --tan-strong: #b98a5e;
    --tan-mid: #d3ae86;
    --tan-light: #e9cba8;
    --tan-pale: #f2dcc0;
    --icon-box: #8f6a48;
    --text-dark: #3b2d22;
    --name-tan: #c99a6c;
    --rule: #6b5645;
    --muted: #b8a898;
  }
  * { box-sizing: border-box; margin: 0; padding: 0; }
  html, body { width: 1200px; height: 800px; overflow: hidden; }
  body {
    background: var(--page-bg);
    font-family: "Roboto", Arial, sans-serif;
    position: relative;
  }
  .card {
    position: absolute;
    top: 250px;
    width: 520px;
    height: 300px;
    background: var(--card-brown);
    border-radius: 4px;
    box-shadow: 0 10px 24px rgba(40, 25, 15, 0.25);
    overflow: hidden;
  }
  .card--front { left: 50px; }
  .card--back { left: 630px; }

  .wordmark {
    color: var(--cream);
    font-weight: 700;
    letter-spacing: 0.5px;
    line-height: 1;
  }
  .card--front .wordmark {
    position: absolute;
    left: 0; right: 0; top: 50%;
    transform: translateY(-50%);
    text-align: center;
    font-size: 64px;
  }

  .person {
    position: absolute;
    left: 40px; top: 34px;
  }
  .person__name {
    font-size: 17px;
    font-weight: 300;
    color: var(--muted);
    letter-spacing: 1px;
  }
  .person__name strong { color: var(--name-tan); font-weight: 700; }
  .person__role {
    font-size: 11px;
    font-weight: 300;
    color: var(--muted);
    margin-top: 3px;
  }
  .divider {
    position: absolute;
    left: 262px; top: 40px;
    width: 1px; height: 120px;
    background: var(--rule);
  }
  .card--back .wordmark {
    position: absolute;
    left: 290px; top: 82px;
    font-size: 44px;
  }

  .contact-bands { position: absolute; left: 0; top: 158px; width: 100%; }
  .band {
    position: relative;
    height: 24px;
    margin-bottom: 4px;
    display: flex;
    align-items: center;
  }
  .band--phone { width: 42%; background: var(--tan-strong); }
  .band--mail { width: 68%; background: var(--tan-light); }
  .band--web { width: 100%; background: var(--tan-pale); }
  .band--plain { width: 100%; background: var(--tan-mid); }
  .band__icon {
    width: 24px; height: 24px;
    margin-left: 40px;
    background: var(--icon-box);
    display: flex; align-items: center; justify-content: center;
    flex: none;
  }
  .band__icon svg { width: 14px; height: 14px; }
  .band__text {
    margin-left: 12px;
    font-size: 13px;
    color: var(--text-dark);
    letter-spacing: 0.3px;
  }
</style>
</head>
<body>

<section class="card card--front" aria-label="Business card front">
  <p class="wordmark">Brushvane</p>
</section>

<section class="card card--back" aria-label="Business card back">
  <div class="person">
    <p class="person__name"><strong>NINA</strong> CORWELL</p>
    <p class="person__role">Designation</p>
  </div>
  <div class="divider"></div>
  <p class="wordmark">Brushvane</p>

  <div class="contact-bands">
    <div class="band band--phone">
      <span class="band__icon">
        <svg viewBox="0 0 16 16" aria-hidden="true"><path d="M4 1.5 6 4.5 4.8 6.2c.8 1.8 2.2 3.2 4 4l1.7-1.2 3 2-1 2.5C8 13.5 2.5 8 3 2.5z" fill="var(--cream)"/></svg>
      </span>
      <span class="band__text">021 48 73 15</span>
    </div>
    <div class="band band--mail">
      <span class="band__icon">
        <svg viewBox="0 0 16 16" aria-hidden="true"><rect x="1.5" y="3.5" width="13" height="9" fill="none" stroke="var(--cream)" stroke-width="1.4"/><path d="M1.5 3.5 8 9l6.5-5.5" fill="none" stroke="var(--cream)" stroke-width="1.4"/></svg>
      </span>
      <span class="band__text">info@brushvane.co.nz</span>
    </div>
    <div class="band band--web">
      <span class="band__icon">
        <svg viewBox="0 0 16 16" aria-hidden="true"><g fill="none" stroke="var(--cream)" stroke-width="1.2"><circle cx="8" cy="8" r="6"/><ellipse cx="8" cy="8" rx="2.6" ry="6"/><path d="M2 8h12M3 5h10M3 11h10"/></g></svg>
      </span>
      <span class="band__text">www.brushvane.co.nz</span>
    </div>
    <div class="band band--plain"></div>
  </div>
</section>

</body>
</html>
```